Tarvell homes and renovations business card design.

Would like some new card designs utilizing my new logo that look professional. I am open to different colors on the logo or utilize the same ones we have. I like the original concept but would like to see some fresh ideas and build on what we have already done.

Target Market(s)

Custom home building industry, Real estate sales, Renovation projects.

Industry/Entity Type

Home Builder

Contact Information for Business Card

Tarvell Homes and Renovations
2871 162nd Street
Cedarholt, Northvale
T0L3P0
Home : 403- 555-0187 Cell: 403- 555-0243

My info is : Gus Tarvell, President and CEO
email: tarvellhomes@quillmail.example
Website: tarvellhomes.example

Requirements
Must have
• Must Use my new logo design. I am open to different colors on the logo or utilize the same ones in the existing design. I can upload the original logo design if needed.

```html
<!DOCTYPE html>
<html lang="en">
<head>
<meta charset="utf-8">
<title>Tarvell Homes and Renovations – Business Card</title>
<link href="https://fonts.googleapis.com/css2?family=Montserrat:wght@600&family=Open+Sans:wght@400;600&display=swap" rel="stylesheet">
<style>
  :root {
    --backdrop: #1e1e1f;
    --card: #131414;
    --gold: #e2ac22;
    --gold-deep: #a97e2c;
    --white: #ffffff;
    --text-light: #e6e6e6;
  }
  * { box-sizing: border-box; margin: 0; padding: 0; }
  html, body {
    width: 1200px; height: 900px; overflow: hidden;
    background: var(--backdrop);
    font-family: "Open Sans", Arial, sans-serif;
  }
  .stage { position: relative; width: 1200px; height: 900px; }
  .card {
    position: absolute; width: 560px; height: 320px;
    background: var(--card); border-radius: 14px; overflow: hidden;
    box-shadow: 0 18px 40px rgba(0,0,0,.55);
  }
  .card--back { left: 60px; top: 110px; }
  .card--front { left: 580px; top: 470px; }

  /* back */
  .accent-line { position: absolute; height: 4px; background: var(--gold); }
  .accent-line--left { left: 0; bottom: 70px; width: 150px; }
  .accent-line--right { right: 0; top: 95px; width: 130px; }
  .wordmark {
    display: flex; align-items: center; gap: 12px;
    font-family: "Montserrat", Arial, sans-serif; font-weight: 600;
    color: var(--gold-deep); text-transform: uppercase; line-height: 1.15;
  }
  .wordmark__square { flex: none; background: var(--gold-deep); }
  .card--back .wordmark {
    position: absolute; left: 150px; top: 118px; width: 270px; font-size: 26px;
  }
  .card--back .wordmark__square { width: 22px; height: 22px; }

  /* front */
  .gold-band { position: absolute; inset: 0; width: 560px; height: 320px; }
  .holder { position: absolute; left: 38px; top: 148px; }
  .holder__name { font-size: 28px; font-weight: 600; color: var(--white); line-height: 1.2; }
  .holder__title { font-size: 13px; color: var(--gold); line-height: 1.3; }
  .contacts { position: absolute; left: 50px; top: 208px; list-style: none; }
  .contacts li {
    display: flex; align-items: flex-start; gap: 9px;
    font-size: 11px; line-height: 14px; color: var(--text-light); margin-bottom: 3px;
  }
  .contacts svg { flex: none; width: 11px; height: 11px; margin-top: 2px; fill: var(--gold); }
  .website {
    position: absolute; left: 38px; top: 292px;
    font-size: 12px; line-height: 16px; color: var(--gold);
  }
  .baseline-rule {
    position: absolute; left: 200px; right: 24px; top: 301px; height: 2px; background: var(--gold);
  }
  .card--front .wordmark {
    position: absolute; right: 28px; top: 196px; width: 190px; font-size: 16px; gap: 9px;
  }
  .card--front .wordmark__square { width: 14px; height: 14px; }
</style>
</head>
<body>
<main class="stage">

  <section class="card card--back" aria-label="Card back">
    <span class="accent-line accent-line--right"></span>
    <div class="wordmark">
      <span class="wordmark__square"></span>
      <span>Tarvell Homes and Renovations</span>
    </div>
    <span class="accent-line accent-line--left"></span>
  </section>

  <section class="card card--front" aria-label="Card front">
    <svg class="gold-band" viewBox="0 0 560 320" aria-hidden="true">
      <polygon points="0,112 560,22 560,50 0,140" fill="#a97e2c"/>
    </svg>

    <div class="holder">
      <p class="holder__name">Gus Tarvell</p>
      <p class="holder__title">President and CEO</p>
    </div>

    <ul class="contacts">
      <li>
        <svg viewBox="0 0 24 24"><path d="M12 2a7 7 0 0 0-7 7c0 5 7 13 7 13s7-8 7-13a7 7 0 0 0-7-7zm0 9.5A2.5 2.5 0 1 1 12 6.5a2.5 2.5 0 0 1 0 5z"/></svg>
        <span>2871 162nd Street<br>Cedarholt, Northvale, T0L3P0</span>
      </li>
      <li>
        <svg viewBox="0 0 24 24"><path d="M3 9c0-3 4-5 9-5s9 2 9 5l-4 1-1-2H8L7 10zM6 11h12l2 9H4z"/></svg>
        <span>403- 555-0187</span>
      </li>
      <li>
        <svg viewBox="0 0 24 24"><path d="M7 1h10a2 2 0 0 1 2 2v18a2 2 0 0 1-2 2H7a2 2 0 0 1-2-2V3a2 2 0 0 1 2-2zm0 3v14h10V4z"/></svg>
        <span>403- 555-0243</span>
      </li>
      <li>
        <svg viewBox="0 0 24 24"><path d="M2 5h20v14H2zm2 2v.5l8 5 8-5V7z"/></svg>
        <span>tarvellhomes@quillmail.example</span>
      </li>
    </ul>

    <p class="website">tarvellhomes.example</p>
    <span class="baseline-rule"></span>

    <div class="wordmark">
      <span class="wordmark__square"></span>
      <span>Tarvell Homes and Renovations</span>
    </div>
  </section>

</main>
</body>
</html>
```